Promotional Flyer for Iron Crane Dialogue

Design a promotional Flyer for Iron Crane Dialogue. Iron Crane Dialogue is a children and teen anti-bullying program. The program is delivered as a term program or as stand alone workshops. Target audience is parent and schools. The program can be delivered for different age groups; 6yr+ 9yrs+ 14yr+ The program will begin in 2017. Details are on the flyers and mock brochure. Bullying is a major problem in Australia for children and teens of all ages starting in primary school through to highschool. In extreme cases it may lead to suicide. I want to make a strong statement and reach out to families who want to help their children and teen by giving them skills and confidence needed to stand up to bullies. Trying to keep it to a one page or two page (back & Front). Need to maintain a martial art ethos but be modern and exciting to look at.
Updates

This is such an important project. I look forward to watching amazing layouts by designers who really see this much more than just another graphic design project but are invested in making a difference for the children and teens who will come through this program. The project is sponsored by Marlow Karate in the Pilbara - Western Australia. check us out https://www.facebook.com/marlowkarateclub/ Thanks Greg

Target Market(s)

parents of children and teens, schools, mental health service providers, government, youth services

Industry/Entity Type

Mental Health

Font styles to use
Sans Serif

Requirements
Must have
• Must have Logos; Iron Crane Dialogue prominent. Must have lesson outline. Must have detail. Must have a martial art ethos Must clearly communicate this is anti-bullying.
Nice to have
• Color - strong anti-bullying message. Clear communication can be delivered in workshops or term based program.
Should not have
• Should not be boring. Not too wordy.

```html
<!DOCTYPE html>
<html lang="en">
<head>
<meta charset="utf-8">
<title>Iron Crane Dialogue – Anti-Bullying for Children &amp; Teens</title>
<link href="https://fonts.googleapis.com/css2?family=Montserrat:wght@300;400;600;800;900&family=Quicksand:wght@500;600;700&family=Roboto+Condensed:wght@700&display=swap" rel="stylesheet">
<style>
  :root {
    --ink: #1c1c1c;
    --red: #e8202a;
    --red-band-start: #e3202b;
    --red-band-end: #f0323e;
    --white: #ffffff;
    --navy: #1b2f6b;
    --orange: #d9782d;
    --photo-light: #e9eef4;
    --photo-mid: #8a8fb0;
    --photo-warm: #d9b8a6;
    --sign-soft: #f6c9cb;
  }
  * { box-sizing: border-box; margin: 0; padding: 0; }
  html, body { width: 851px; height: 1200px; overflow: hidden; background: var(--white); }
  .flyer { position: relative; width: 851px; height: 1200px; background: var(--white); color: var(--ink); font-family: "Quicksand", sans-serif; }

  /* Header brand */
  .brand { position: absolute; left: 32px; top: 22px; display: flex; align-items: center; gap: 30px; }
  .brand-mark { width: 150px; height: 150px; background: var(--ink); }
  .brand-name { font-family: "Montserrat", sans-serif; font-weight: 800; font-size: 68px; line-height: 0.98; letter-spacing: -1px; color: var(--ink); text-transform: uppercase; }

  .tagline { position: absolute; left: 60px; top: 180px; display: flex; align-items: baseline; gap: 22px; }
  .tagline-main { font-family: "Montserrat", sans-serif; font-weight: 900; font-size: 41px; color: var(--red); letter-spacing: 0.5px; }
  .tagline-sub { font-family: "Montserrat", sans-serif; font-weight: 400; font-size: 27px; color: var(--ink); letter-spacing: 1px; }

  /* Red info band */
  .info-band { position: absolute; left: 0; top: 234px; width: 851px; height: 281px; background: linear-gradient(90deg, var(--red-band-start), var(--red-band-end)); color: var(--white); }
  .intro { position: absolute; left: 40px; top: 15px; width: 292px; font-size: 15.4px; line-height: 18.5px; text-align: justify; font-weight: 500; }
  .lessons { position: absolute; left: 360px; top: 15px; }
  .lessons-title { font-family: "Montserrat", sans-serif; font-weight: 800; font-size: 16.4px; letter-spacing: 0.2px; margin-bottom: 9px; }
  .lessons-list { list-style: none; }
  .lessons-list li { font-size: 16.6px; line-height: 21.6px; font-weight: 500; display: flex; white-space: nowrap; }
  .lessons-list .num { font-family: "Montserrat", sans-serif; font-weight: 800; width: 28px; font-size: 14.5px; }

  /* Hero area */
  .hero { position: absolute; left: 0; top: 515px; width: 851px; height: 453px; overflow: hidden; }
  .hero-photo { position: absolute; inset: 0; background:
      linear-gradient(90deg, var(--white) 0%, rgba(255,255,255,0.85) 28%, rgba(255,255,255,0) 52%),
      radial-gradient(ellipse at 82% 60%, var(--photo-warm) 0%, rgba(217,184,166,0) 45%),
      linear-gradient(90deg, var(--photo-light) 30%, var(--photo-mid) 60%, #6b5fa0 78%, #c9cdd8 100%); }
  .hero-year { position: absolute; left: 64px; top: 62px; font-family: "Montserrat", sans-serif; font-weight: 900; font-size: 31px; color: var(--ink); }
  .sign-graphic { position: absolute; left: 52px; top: 108px; width: 266px; height: 266px; background: linear-gradient(160deg, var(--sign-soft), rgba(246,201,203,0.35)); }
  .sign-word { position: absolute; left: 46px; top: 212px; font-family: "Montserrat", sans-serif; font-weight: 900; font-size: 56px; letter-spacing: -1px; color: var(--ink); }
  .hero-shout { position: absolute; left: 64px; top: 378px; font-family: "Roboto Condensed", sans-serif; font-weight: 700; font-size: 30px; color: var(--ink); }

  /* Details */
  .details { position: absolute; left: 35px; top: 1021px; font-size: 16.4px; line-height: 21.6px; font-weight: 500; }
  .details-row { display: flex; white-space: nowrap; }
  .details-label { font-family: "Montserrat", sans-serif; font-weight: 800; width: 141px; font-size: 14.6px; }
  .details-row.contact .details-label { width: auto; margin-right: 6px; }

  /* Partners */
  .partners { position: absolute; left: 612px; top: 1004px; width: 220px; height: 190px; }
  .partner-edu { position: absolute; left: 34px; top: 16px; font-family: "Montserrat", sans-serif; font-weight: 800; font-size: 19px; color: var(--navy); line-height: 1.05; text-align: center; }
  .partner-club { position: absolute; left: 0; top: 116px; width: 110px; font-family: "Montserrat", sans-serif; font-weight: 800; font-size: 16px; line-height: 1.1; color: var(--ink); text-align: center; }
  .partner-badge { position: absolute; left: 118px; top: 90px; width: 82px; height: 82px; border-radius: 50%; background: var(--orange); }
</style>
</head>
<body>
<div class="flyer">

  <header class="brand">
    <div class="brand-mark"></div>
    <div class="brand-name">Iron Crane<br>Dialogue</div>
  </header>

  <div class="tagline">
    <span class="tagline-main">ANTI-BULLYING</span>
    <span class="tagline-sub">FOR CHILDREN &amp; TEENS</span>
  </div>

  <section class="info-band">
    <p class="intro">&nbsp;&nbsp;Iron Crane Dialogue provides anti-bullying workshops and term based programs that will engage, equip, and empower your child &amp; teen with skills and confidence needed to stop bullying and build effective communication skills and relationships based upon respect &amp; responsibility. Iron Crane Dialogue combines the ethos of martial arts training with the teaching methods of the acclaimed "Stone &amp; Stream" antibullying program developed by the Veldhoven Institute in Holland.</p>
    <div class="lessons">
      <h2 class="lessons-title">10 LESSONS IN IRON CRANE DIALOGUE</h2>
      <ol class="lessons-list">
        <li><span class="num">1.</span>Iron Crane Dialogue Code</li>
        <li><span class="num">2.</span>Stone &amp; Stream Relationships</li>
        <li><span class="num">3.</span>Foundations 4 Standing Strong</li>
        <li><span class="num">4.</span>Breathing &amp; Balance Under Pressure</li>
        <li><span class="num">5.</span>Self Defence (Persuasion &amp; Evasion)</li>
        <li><span class="num">6.</span>Friend or Foe (Boundaries for All)</li>
        <li><span class="num">7.</span>Don't Be a Bystander: How to Give and Get Help</li>
        <li><span class="num">8.</span>Resistance or Resilience</li>
        <li><span class="num">9.</span>Inner Compass: Navigating Relationships</li>
        <li><span class="num">10.</span>Iron Crane Leadership</li>
      </ol>
    </div>
  </section>

  <section class="hero">
    <div class="hero-photo" role="img" aria-label="Photo: a sad schoolboy holding a purple folder in a school corridor while classmates whisper behind him"></div>
    <div class="hero-year">2017 PILBARA</div>
    <div class="sign-graphic" role="img" aria-label="Graphic: red prohibition sign crossing out bullying"></div>
    <div class="sign-word">BULLYING</div>
    <div class="hero-shout">ENOUGH ALREADY!</div>
  </section>

  <section class="details">
    <div class="details-row"><span class="details-label">LOCATION:</span>Kestrel Community Centre</div>
    <div class="details-row"><span class="details-label">TIME:</span>Every Saturday morning/afternoon. (45min lessons)</div>
    <div class="details-row"><span class="details-label">REGISTRATION:</span>Jan 2017 CLASS START: February 2017</div>
    <div class="details-row"><span class="details-label">COST:</span>$150 per term + $50 Equipment</div>
    <div class="details-row"><span class="details-label">AGES:</span>6yrs+ 9yrs+ 14yrs+ (min 10 - max 20 per class)</div>
    <div class="details-row"><span class="details-label">TRAINER:</span>Greg Saunders (Stone&amp;Stream Facilitator / 3rd Dan TKD)</div>
    <div class="details-row contact"><span class="details-label">CONTACT:</span>greg@ironcranedialogue.com or 0491570156</div>
  </section>

  <aside class="partners">
    <div class="partner-edu">LEARNWELL<br>PARTNERS</div>
    <div class="partner-club">MARLOW KARATE</div>
    <div class="partner-badge"></div>
  </aside>

</div>
</body>
</html>
```